Modern Business Card Design Needed for Young Realtor

Information that is going on the card:Marvin Pold
Broker/Owner
555.210.3367
Marvin@MPoldRealty.com
www.MPoldRealty.com

Would also like to include my Instagram Handle somewhere. Probably on the back: the_queencity_realtorMy previous business card is attached, I like that one but would like an updated version and maybe a few design changes

Marvin Pold
Broker/Owner
555.210.3367
Marvin@MPoldRealty.com
www.MPoldRealty.com

• Would also like to include my Instagram Handle somewhere. Probably on the back: the_pinecrest_realtor
• Dorrance Hale or the DH (logo from the previous card.)

```html
<!DOCTYPE html>
<html lang="en">
<head>
<meta charset="utf-8">
<title>MPold Realty – Business Card</title>
<link href="https://fonts.googleapis.com/css2?family=Roboto:wght@400;500;700&display=swap" rel="stylesheet">
<style>
  :root {
    --backdrop: #232323;
    --card: #1d1b1c;
    --ink: #ececec;
    --ink-soft: #d6d6d6;
    --photo-light: #e4e4e2;
    --photo-mid: #8a8a88;
    --photo-dark: #4e4e50;
  }
  * { margin: 0; padding: 0; box-sizing: border-box; }
  html, body {
    width: 1200px; height: 896px; overflow: hidden;
    background: var(--backdrop);
    font-family: "Roboto", Arial, sans-serif;
    color: var(--ink);
  }
  .card {
    position: absolute; left: 353px; width: 486px; height: 277px;
    background: var(--card);
    box-shadow: 0 8px 22px rgba(0,0,0,0.55);
  }
  .card--front { top: 160px; }
  .card--back { top: 469px; }

  .portrait {
    position: absolute; left: 0; top: 0; width: 206px; height: 277px;
    background: linear-gradient(180deg, var(--photo-light) 0%, var(--photo-light) 38%, var(--photo-mid) 70%, var(--photo-dark) 100%);
  }

  .brand {
    display: flex; align-items: center; gap: 7px;
    font-weight: 400; color: var(--ink);
    text-transform: uppercase; white-space: nowrap;
  }
  .brand__mark { background: var(--ink); flex: none; }

  .card--front .brand {
    position: absolute; left: 252px; top: 80px;
    font-size: 18px; letter-spacing: 3.6px;
  }
  .card--front .brand__mark { width: 8px; height: 8px; }

  .identity { position: absolute; left: 251px; top: 129px; }
  .identity__name { font-size: 14.5px; font-weight: 700; line-height: 18px; }
  .identity__role { font-size: 10.5px; font-weight: 400; color: var(--ink-soft); line-height: 13px; }

  .contacts { position: absolute; left: 251px; top: 176px; list-style: none; }
  .contacts li {
    display: flex; align-items: center; gap: 7px;
    font-size: 10.5px; line-height: 14px; color: var(--ink-soft);
  }
  .contacts svg { width: 8px; height: 8px; flex: none; }

  .card--back .brand {
    position: absolute; left: 0; right: 0; top: 134px;
    justify-content: center; font-size: 28px; letter-spacing: 6px;
  }
  .card--back .brand__mark { width: 12px; height: 12px; }

  .social {
    position: absolute; left: 0; right: 0; top: 225px;
    display: flex; justify-content: center; align-items: center; gap: 5px;
    font-size: 10.5px; color: var(--ink-soft);
  }
  .social__mark { width: 8px; height: 8px; background: var(--ink-soft); }
</style>
</head>
<body>
  <section class="card card--front">
    <div class="portrait" role="img" aria-label="Portrait photo of Marvin Pold in a grey blazer against a light wall"></div>

    <div class="brand"><span class="brand__mark"></span>MPold Realty</div>

    <div class="identity">
      <p class="identity__name">Marvin Pold</p>
      <p class="identity__role">Broker/Owner</p>
    </div>

    <ul class="contacts">
      <li>
        <svg viewBox="0 0 10 10" aria-hidden="true"><path d="M2 1 L4 1 L4.6 3.2 L3.5 4 Q4.5 6 6 6.5 L6.8 5.4 L9 6 L9 8 Q8.5 9 7.5 9 Q1 8 1 2 Q1 1 2 1 Z" fill="#d6d6d6"/></svg>
        555.210.3367
      </li>
      <li>
        <svg viewBox="0 0 10 10" aria-hidden="true"><rect x="0.7" y="2" width="8.6" height="6" fill="none" stroke="#d6d6d6" stroke-width="1"/><path d="M0.7 2 L5 5.5 L9.3 2" fill="none" stroke="#d6d6d6" stroke-width="1"/></svg>
        Marvin@MPoldRealty.com
      </li>
      <li>
        <svg viewBox="0 0 10 10" aria-hidden="true"><circle cx="5" cy="5" r="4.2" fill="none" stroke="#d6d6d6" stroke-width="0.9"/><ellipse cx="5" cy="5" rx="1.8" ry="4.2" fill="none" stroke="#d6d6d6" stroke-width="0.8"/><path d="M0.8 5 H9.2" stroke="#d6d6d6" stroke-width="0.8"/></svg>
        www.MPoldRealty.com
      </li>
    </ul>
  </section>

  <section class="card card--back">
    <div class="brand"><span class="brand__mark"></span>MPold Realty</div>
    <p class="social"><span class="social__mark"></span>the_pinecrest_realtor</p>
  </section>
</body>
</html>
```